Banner Ad for Pilot Life Insurance

Cirrus Assurance Group (www.halvenorcover.example). We sell life insurance products to pilots in the United States market. Life Insurance is a highly regulated business so the promises or claims made in advertising is required to be accurate. This is a banner ad for the site skyroutelog.example. It is going in the section Fast Facts.

• 600w x 300h
• 200 kb maximum file size.
• 72dpi, GIF or JPG format.
• Animation is acceptable (15 second maximum).
• Audio can NOT be used.
• Expandable ads are not accepted.
• Flash is not recommended unless the URL click-through is embedded.
• JavaScript is not accepted.

Link to other stuff we have done:
https://www.filevaultshare.example/sh/qx7trmbnoe2kdzy/hLP4wzRu_k

Target Market(s)

Audience is 95% male 40 to 65 year of age in the United States - all are pilots most as their profession.

Industry/Entity Type

Life Insurance

Requirements
Must have
• Banner advertising is not something that has been effective for us in the past. Our best advertising efforts today have been in newsletters with embeded text ads and email industry information newsletters. So it needs something to get attention or call to action.

```html
<!DOCTYPE html>
<html lang="en">
<head>
<meta charset="utf-8">
<title>Cirrus Assurance Group – Pilot Life Insurance Banner</title>
<link rel="stylesheet" href="https://fonts.googleapis.com/css2?family=PT+Sans:wght@400;700&family=PT+Sans+Narrow:wght@400;700&display=swap">
<style>
  :root {
    --sky-top: #4f9ad8;
    --sky-mid: #8cc3ec;
    --sky-light: #c9e4f7;
    --band-top: #e3f0fa;
    --band-bottom: #bcdcf2;
    --navy: #1b2f6e;
    --white: #ffffff;
    --photo-sky: #b5d9f3;
    --photo-mid: #98b6cc;
    --photo-jacket: #7a5e4c;
  }
  * { margin: 0; padding: 0; box-sizing: border-box; }
  html, body { width: 1200px; height: 600px; overflow: hidden; background: var(--white); }
  .banner {
    position: relative;
    width: 1200px;
    height: 600px;
    overflow: hidden;
    background: linear-gradient(100deg, var(--sky-top) 0%, var(--sky-mid) 55%, var(--sky-light) 100%);
    font-family: "PT Sans", Arial, sans-serif;
  }
  .hero-photo {
    position: absolute;
    left: 580px;
    top: 0;
    width: 620px;
    height: 392px;
    background: linear-gradient(155deg, var(--photo-sky) 0%, var(--photo-mid) 50%, var(--photo-jacket) 100%);
    -webkit-mask-image: linear-gradient(to right, transparent 0%, #000 35%);
    mask-image: linear-gradient(to right, transparent 0%, #000 35%);
  }
  .headline {
    position: absolute;
    left: 50px;
    top: 40px;
    color: var(--white);
    line-height: 1;
    font-weight: 400;
  }
  .headline__lead { display: block; font-size: 44px; }
  .headline__key { display: block; font-size: 116px; letter-spacing: 1px; margin-top: 2px; }
  .headline__product { display: block; font-size: 54px; margin-top: 4px; }
  .benefits {
    position: absolute;
    left: 52px;
    top: 300px;
    color: var(--white);
    font-family: "PT Sans Narrow", Arial, sans-serif;
    font-weight: 700;
    font-size: 25px;
    letter-spacing: 0.5px;
  }
  .benefits__dot { margin: 0 12px; }
  .contact-band {
    position: absolute;
    left: 0;
    top: 392px;
    width: 1200px;
    height: 208px;
    background: linear-gradient(180deg, var(--band-top) 0%, var(--band-bottom) 100%);
  }
  .brand {
    position: absolute;
    left: 60px;
    top: 468px;
    display: flex;
    align-items: center;
    gap: 12px;
  }
  .brand__mark { width: 30px; height: 30px; border-radius: 50%; background: var(--navy); flex: none; }
  .brand__name {
    color: var(--navy);
    font-weight: 700;
    font-size: 19px;
    line-height: 1.15;
    text-transform: uppercase;
    width: 180px;
  }
  .phone {
    position: absolute;
    left: 344px;
    top: 444px;
    color: var(--navy);
    font-weight: 700;
    font-size: 50px;
    letter-spacing: 0.5px;
  }
  .site-url {
    position: absolute;
    left: 346px;
    top: 520px;
    color: var(--navy);
    font-weight: 700;
    font-size: 21px;
  }
</style>
</head>
<body>
<div class="banner">
  <div class="hero-photo" role="img" aria-label="Photo of a child in a leather flying jacket, cap and goggles with arms spread like wings against a blue sky"></div>

  <h1 class="headline">
    <span class="headline__lead">Get the</span>
    <span class="headline__key">RIGHT</span>
    <span class="headline__product">Pilot Life Insurance</span>
  </h1>

  <p class="benefits">LOWER RATES<span class="benefits__dot">•</span>NO AVIATION EXCLUSIONS</p>

  <div class="contact-band"></div>

  <div class="brand">
    <span class="brand__mark"></span>
    <span class="brand__name">Cirrus Assurance Group</span>
  </div>

  <p class="phone">1-800-555-0142</p>
  <p class="site-url">WWW.HALVENORCOVER.EXAMPLE</p>
</div>
</body>
</html>
```